Storage Company Newsletter

We need a design for a newsletter for our company Vaultnest, a digital and physical asset storage company .The newsletter will be informative and educational covering tips on secure storage of personal documents and items both at home and at the work place. Rest easy with Vaultnest is our mantra. We have a pre-existing trademark & logo. Colors are blue and green. We can share the cmyk/rgb color information and background is grey.

Target Market(s)

Mass market – Middle to High income individuals

Industry/Entity Type

Digital

Font styles to use
Sans Serif

Colors
0393ce
00a88f
edf2f7

Requirements
Must have
• The newsletter linked to a CMS. In HTML5; Mail-chimp integration readable on Gmail, Yahoo, Hotmail and Outlook
Nice to have
• Sections of the newsletter are:
• Cover story
• News Flash
• Mwanachi Perspective
• Spotlight on the Counties
• CEO's Corner
• Tips and Helpful Information
• Important Dates and Events

```html
<!DOCTYPE html>
<html lang="en">
<head>
<meta charset="utf-8">
<title>Vaultnest Newsletter</title>
<link rel="stylesheet" href="https://fonts.googleapis.com/css2?family=Arimo:wght@400;700&family=Open+Sans:wght@600&display=swap">
<style>
  :root {
    --teal: #00a88f;
    --teal-dark: #00806c;
    --blue: #0393ce;
    --band: #edf2f7;
    --ink: #3f3f3a;
    --body: #4a4a4a;
    --muted: #9a9a9a;
    --rule: #8c8475;
    --faint: #dcdcdc;
    --ribbon: #d8141b;
    --paper: #ffffff;
  }
  * { box-sizing: border-box; margin: 0; padding: 0; }
  html, body { width: 723px; height: 1200px; overflow: hidden; background: var(--paper); }
  body { position: relative; font-family: "Arimo", Arial, sans-serif; color: var(--body); }
  .abs { position: absolute; }

  .masthead { left: 12px; top: 9px; width: 699px; height: 224px;
    background: radial-gradient(ellipse at 45% 40%, #10b596 0%, #078f7a 55%, #046a5b 100%); overflow: hidden; }
  .brand { left: 64px; top: 88px; display: flex; align-items: center; gap: 10px;
    font-size: 26px; font-weight: 700; color: #ffffff; }
  .brand-mark { width: 22px; height: 22px; background: var(--blue); border-radius: 50%; }
  .hero-art { left: 390px; top: 40px; width: 230px; height: 175px;
    background: linear-gradient(160deg, #fafafa, #cfd4d3); border-radius: 4px; }
  .ribbon { right: 0; top: 13px; width: 182px; height: 33px; }
  .ribbon-label { right: 10px; top: 22px; font-size: 12px; color: #fff; letter-spacing: .2px; }

  .cover { left: 12px; top: 233px; width: 699px; height: 161px; background: var(--band); }
  .section-title { font-weight: 400; color: var(--ink); letter-spacing: -.5px; }
  .cover-title { left: 30px; top: 240px; font-size: 29px; }
  .cover-text { left: 30px; top: 279px; width: 430px; font-size: 10.6px; line-height: 16.5px; color: var(--body); }
  .events-title { left: 497px; top: 245px; font-size: 21px; }
  .events { left: 493px; top: 276px; width: 210px; list-style: none; }
  .events li { display: flex; gap: 10px; font-size: 10.5px; line-height: 12.5px; color: #222; margin-bottom: 13px; }
  .events svg { flex: 0 0 auto; margin-top: 1px; }

  .tip { width: 202px; }
  .tip-photo { height: 81px; }
  .tip-text { margin-top: 12px; font-size: 10.4px; line-height: 16.2px; color: var(--muted); padding-left: 2px; }
  .divider-dotted { width: 0; border-left: 1px dotted #b7b7b7; height: 214px; top: 412px; }

  .rule { left: 12px; width: 699px; height: 1px; background: var(--rule); }
  .ceo-photo { left: 20px; top: 659px; width: 207px; height: 111px;
    background: linear-gradient(100deg, #6e2c5c 0%, #8a4f6a 40%, #c9a087 70%, #e2c7a2 100%); }
  .ceo-title { left: 242px; top: 659px; font-size: 29px; }
  .ceo-text { left: 242px; top: 698px; width: 460px; font-size: 10.5px; line-height: 15.3px; color: var(--body); }

  .feature { top: 817px; width: 220px; height: 223px; border: 1px solid #d8d8d8; border-top: 0; background: var(--paper); }
  .feature-head { height: 36px; margin: 0 -1px; display: flex; align-items: center; gap: 9px; padding-left: 9px;
    background: linear-gradient(#1cb69c, var(--teal-dark)); font-family: "Open Sans", Arial, sans-serif;
    font-weight: 600; font-size: 12px; color: #fff; box-shadow: 0 4px 5px -3px rgba(0,0,0,.35); }
  .feature-text { padding: 19px 11px 0; font-size: 10.4px; line-height: 16.2px; color: var(--body); }

  .footer-band { left: 12px; top: 1065px; width: 699px; height: 4px; background: #eeeee4; }
  .subscribe { left: 15px; top: 1076px; width: 134px; height: 28px; background: var(--teal-dark);
    color: #fff; font-family: "Open Sans", Arial, sans-serif; font-weight: 600; font-size: 12.5px;
    display: flex; align-items: center; justify-content: center; }
  .social { top: 1076px; width: 29px; height: 29px; }
  .social-a { left: 617px; background: #3b5998; }
  .social-b { left: 650px; background: #39a9e0; }
  .social-c { left: 683px; background: #2f6f8f; }
  .legal { left: 15px; top: 1130px; width: 430px; font-size: 9.6px; line-height: 13.5px; color: var(--faint); }
  .legal p + p { margin-top: 2px; }
  .copyright { right: 10px; top: 1157px; font-size: 9.8px; color: #c8c8c8; }
</style>
</head>
<body>
  <header class="abs masthead">
    <div class="abs brand"><span class="brand-mark"></span>Vaultnest</div>
    <div class="abs hero-art" role="img" aria-label="Photo of a tall stack of loose paper documents"></div>
    <svg class="abs ribbon" viewBox="0 0 182 33" aria-hidden="true">
      <polygon points="0,0 182,0 182,33 22,33" fill="var(--ribbon)"/>
      <polygon points="0,0 22,33 14,33" fill="#8e0d12"/>
    </svg>
    <span class="abs ribbon-label">// NEWSLETTER ARTICLE 1</span>
  </header>

  <section class="abs cover"></section>
  <h1 class="abs section-title cover-title">cover story</h1>
  <p class="abs cover-text">Valuable documents include a wide range of items such as landtitle deeds, certificates, letters, photographs, newspaper cuttings andmemorabilia. The longevity of these items can be threatened by numerous factorssuch as light, moisture, insects such as silverfish, and physical damage.&nbsp; By taking these simple precautions outlinedbelow, you can preserve your valuable documents and keep them for posterity.</p>

  <h2 class="abs section-title events-title">important events</h2>
  <ul class="abs events">
    <li><svg width="18" height="18" viewBox="0 0 18 18"><circle cx="9" cy="9" r="7.5" fill="none" stroke="var(--blue)" stroke-width="1.6"/><polygon points="7,5.5 12.5,9 7,12.5" fill="var(--blue)"/></svg><span>Lorem ipsum dolor sit amet,<br>consectetur adipiscing elit.</span></li>
    <li><svg width="18" height="18" viewBox="0 0 18 18"><circle cx="9" cy="9" r="7.5" fill="none" stroke="var(--blue)" stroke-width="1.6"/><polygon points="7,5.5 12.5,9 7,12.5" fill="var(--blue)"/></svg><span>Lorem ipsum dolor sit amet,<br>consectetur adipiscing elit.</span></li>
    <li><svg width="18" height="18" viewBox="0 0 18 18"><circle cx="9" cy="9" r="7.5" fill="none" stroke="var(--blue)" stroke-width="1.6"/><polygon points="7,5.5 12.5,9 7,12.5" fill="var(--blue)"/></svg><span>Lorem ipsum dolor sit amet,<br>consectetur adipiscing elit.</span></li>
  </ul>

  <article class="abs tip" style="left:20px; top:412px;">
    <div class="tip-photo" role="img" aria-label="Photo of colourful numbered file folders on a shelf" style="background:linear-gradient(90deg,#f3d9a8,#e0436a 45%,#f0b23a 75%,#f7ecd2);"></div>
    <p class="tip-text">Valuabledocuments should be stored off the floor and away from external walls orwindows, to protect them from dramatic fluctuations in temperature andhumidity. Storage areas must remain dry to prevent mould growth and waterdamage.</p>
  </article>
  <div class="abs divider-dotted" style="left:240px;"></div>
  <article class="abs tip" style="left:260px; top:412px;">
    <div class="tip-photo" role="img" aria-label="Photo of a hand pressing buttons on an office fax machine" style="background:linear-gradient(120deg,#5d6d7a,#c9d3da 45%,#eef2f5 75%,#8fa2b0);"></div>
    <p class="tip-text">Valuabledocuments should be stored off the floor and away from external walls orwindows, to protect them from dramatic fluctuations in temperature andhumidity. Storage areas must remain dry to prevent mould growth and waterdamage.</p>
  </article>
  <div class="abs divider-dotted" style="left:481px;"></div>
  <article class="abs tip" style="left:500px; top:412px;">
    <div class="tip-photo" role="img" aria-label="Photo of printed pages running through a printing press" style="background:linear-gradient(160deg,#3e3a45,#b9b4b8 45%,#e9e3e0 70%,#c58b8b);"></div>
    <p class="tip-text">Valuabledocuments should be stored off the floor and away from external walls orwindows, to protect them from dramatic fluctuations in temperature andhumidity. Storage areas must remain dry to prevent mould growth and waterdamage.</p>
  </article>

  <div class="abs rule" style="top:638px;"></div>
  <div class="abs ceo-photo" role="img" aria-label="Portrait photo of the company CEO in a suit"></div>
  <h2 class="abs section-title ceo-title">ceo’s corner</h2>
  <p class="abs ceo-text">As a public company, we are responsible for driving our business forward to the benefit of all our stakeholders and providing our stockholders with a return on their investment commensurate with our valuation as a premier industrial company. This will only be accomplished by our continued focus on quality, reliability, durability, vocational value and customer service.</p>
  <div class="abs rule" style="top:789px;"></div>

  <section class="abs feature" style="left:12px;">
    <div class="feature-head"><svg width="16" height="16" viewBox="0 0 16 16"><circle cx="8" cy="8" r="6.8" fill="none" stroke="#0b5e50" stroke-width="1.6"/><polygon points="6.3,4.8 11,8 6.3,11.2" fill="#0b5e50"/></svg>Mwanachi Perspective</div>
    <p class="feature-text">Lorem Ipsum is simply dummy text of the printing and typesetting industry. Lorem Ipsum has been the industry’s standard dummy text ever since the 1500s, when an unknown printer took a galley of type and scrambled it to make a type specimen book.</p>
  </section>
  <section class="abs feature" style="left:252px;">
    <div class="feature-head"><svg width="16" height="16" viewBox="0 0 16 16"><circle cx="8" cy="8" r="6.8" fill="none" stroke="#0b5e50" stroke-width="1.6"/><polygon points="6.3,4.8 11,8 6.3,11.2" fill="#0b5e50"/></svg>Spotlight on the Counties</div>
    <p class="feature-text">Lorem Ipsum is simply dummy text of the printing and typesetting industry. Lorem Ipsum has been the industry’s standard dummy text ever since the 1500s, when an unknown printer took a galley of type and scrambled it to make a type specimen book.</p>
  </section>
  <section class="abs feature" style="left:491px;">
    <div class="feature-head"><svg width="16" height="16" viewBox="0 0 16 16"><circle cx="8" cy="8" r="6.8" fill="none" stroke="#0b5e50" stroke-width="1.6"/><polygon points="6.3,4.8 11,8 6.3,11.2" fill="#0b5e50"/></svg>Helpful Information</div>
    <p class="feature-text">Lorem Ipsum is simply dummy text of the printing and typesetting industry. Lorem Ipsum has been the industry’s standard dummy text ever since the 1500s, when an unknown printer took a galley of type and scrambled it to make a type specimen book.</p>
  </section>

  <footer>
    <div class="abs footer-band"></div>
    <div class="abs subscribe">SUBSCRIBE</div>
    <span class="abs social social-a" aria-label="Social link"></span>
    <span class="abs social social-b" aria-label="Social link"></span>
    <span class="abs social social-c" aria-label="Social link"></span>
    <div class="abs legal">
      <p>You are currently subscribed to receive newsletter&nbsp; from valuable documents, we respects your privacy and does not share any information about you with other parties.</p>
      <p>You can unsubscribe from this email or modify your subscription settings at any time.</p>
    </div>
    <p class="abs copyright">© valuable documents,&nbsp; All Rights Reserved</p>
  </footer>
</body>
</html>
```